New Business Card Design Project

We need to enhance the look and feel of our brand. We are starting with the business card and will hopefully expand to letter head, website, etc. The firm is based in Kolding Denmark and invests with global pension funds and for mutual fund investors alike. We would like to see an innovative use of the companies logo (star on the website - www.northmerrowcap.com) and a broader use of a color palette. Presently it is dominantly shades of blue. The firm wants to convey a sense they are a creative investment team that understands all the risks in the emerging markets and have the skills to perform in an environment of uncertainty.

Presently, we have three locations: Kolding Denmark, Glendale CA USA, Zurich Switzerland. We also have a prominently displayed bar code square on a solid dark blue back that will take smart phone users to the firm's website. I am indifferent to its inclusion., Details for my new Business Card Design Project will be added soon.
Updates

Project Deadline Extended
Reason: Designers, I am working with on getting feedback from both US and Danish partners on preferences. That is taking slightly more time than expected. Thanks for you patience. Nice work. TLV

Target Market(s)

The target market is a combination of institutional and retail investors. The european arm uses a card similar to a couple of those submitted.

Industry/Entity Type

Environment

Requirements
Must have
• The company's Star Logo. See www.northmerrowcap.com. It may be used in its current form or some new clever way. The founders are Danish and have a strong affinity for it.
Nice to have
• The new materials may be solely used in the north America and distributed in Australia as well. Therefore, we may try something new in these markets. I'd prefer to see a broader use of the color spectrum, not simply blue.
Should not have
• The card should not look and feel like a bank, insurance company, or a traditional money manager.

```html
<!DOCTYPE html>
<html lang="en">
<head>
<meta charset="utf-8">
<title>NorthMerrow – Business Card Options</title>
<link rel="stylesheet" href="https://fonts.googleapis.com/css2?family=Arimo&family=Cabin:wght@500;700&display=swap">
<style>
  :root{
    --page:#ffffff;
    --navy:#0d2a5c;
    --mark:#14386e;
    --ring:#1c5fa8;
    --sky:#bfe3f2;
    --sky-deep:#2f8fd6;
    --leaf:#b9dd9a;
    --mint:#2fd27a;
    --blush:#f4e3ef;
    --violet:#b07cc0;
    --violet-deep:#7a58b0;
    --lilac:#d9c6e6;
    --aqua:#8fdbe6;
    --gold:#f3bf1f;
    --sand:#efe2b2;
    --orange:#ec7a1c;
    --sage:#cfd8c2;
    --olive:#a9b48a;
    --text-light:#ffffff;
  }
  *{box-sizing:border-box;margin:0;padding:0}
  html,body{width:777px;height:1200px;overflow:hidden;background:var(--page)}
  .sheet{position:relative;width:777px;height:1200px}
  .option-number{position:absolute;font-family:"Arimo",Arial,sans-serif;font-size:33px;color:#111;line-height:1}
  .card{position:absolute;width:287px;height:164px;overflow:hidden}
  .col-left{left:73px}.col-right{left:433px}
  .map-area{position:absolute;inset:0}
  .brand{position:absolute;display:flex;align-items:center;gap:6px;font-family:"Cabin",sans-serif;font-weight:700;color:var(--mark);white-space:nowrap}
  .brand-dot{border-radius:50%;background:var(--ring);flex:none}
  .brand.stacked{flex-direction:column;gap:6px;left:0;right:0}
  .tagline{position:absolute;left:0;right:0;font-family:"Cabin",sans-serif;font-weight:500;font-size:6.6px;line-height:1.35;padding:0 12px;color:var(--text-light)}
  .caps{text-transform:uppercase}
  .band{position:absolute;left:0;right:0}
  svg.shape{position:absolute;inset:0;width:100%;height:100%}
</style>
</head>
<body>
<main class="sheet">

  <!-- Option 1 -->
  <span class="option-number" style="left:35px;top:56px">1</span>
  <section class="card col-left" style="top:58px;background:linear-gradient(90deg,var(--leaf) 0 45%,var(--sky) 45%)">
    <div class="map-area" role="img" aria-label="Faint world map" style="left:8px;right:8px;top:18px;bottom:28px;border-radius:40px 40px 0 0;background:radial-gradient(ellipse at 50% 50%,#ffffff 0 45%,#dff0f8 100%)"></div>
    <div class="brand stacked" style="top:30px;font-size:24px"><span class="brand-dot" style="width:44px;height:44px"></span>NorthMerrow</div>
    <div class="band" style="bottom:0;height:30px;background:var(--navy)"></div>
    <p class="tagline caps" style="bottom:6px">The new materials may be solely used in the North America and distributed in Australia as well. Therefore, we may try something new in these markets.</p>
  </section>

  <!-- Option 2 -->
  <span class="option-number" style="left:35px;top:266px">2</span>
  <section class="card col-left" style="top:291px;background:linear-gradient(180deg,#fbf6fa,var(--blush))">
    <div class="map-area" role="img" aria-label="Faint pink world map" style="background:radial-gradient(ellipse at 50% 35%,#f8eef5 0 40%,#ecd6e6 100%);opacity:.8"></div>
    <svg class="shape" viewBox="0 0 287 164" preserveAspectRatio="none"><path d="M0 164V110Q0 134 40 134H287V164Z" fill="var(--navy)"/></svg>
    <div class="brand stacked" style="top:10px;font-size:26px"><span class="brand-dot" style="width:46px;height:46px"></span>NorthMerrow</div>
    <p class="tagline" style="bottom:6px;padding-left:14px;font-size:6.8px">The new materials may be solely used in the North America and distributed in Australia as well. Therefore, we may try something new in these markets.</p>
  </section>

  <!-- Option 3 -->
  <span class="option-number" style="left:35px;top:480px">3</span>
  <section class="card col-left" style="top:530px;background:var(--aqua)">
    <div class="map-area" role="img" aria-label="Purple world map over city skyline" style="bottom:40px;background:linear-gradient(180deg,var(--lilac),var(--violet))"></div>
    <svg class="shape" viewBox="0 0 287 164" preserveAspectRatio="none"><path d="M0 106Q143 144 287 106V164H0Z" fill="#ffffff"/><path d="M0 112Q143 150 287 112V164H0Z" fill="var(--aqua)"/></svg>
    <div class="brand stacked" style="top:34px;font-size:20px;color:#3c6fb0"><span class="brand-dot" style="width:32px;height:32px"></span>NorthMerrow</div>
    <p class="tagline caps" style="bottom:8px;font-size:6.2px">The new materials may be solely used in the North America and distributed in Australia as well. Therefore, we may try something new in these markets.</p>
  </section>

  <!-- Option 4 -->
  <span class="option-number" style="left:35px;top:718px">4</span>
  <section class="card col-left" style="top:767px">
    <div class="map-area" role="img" aria-label="Violet world map over city skyline" style="background:linear-gradient(180deg,#dcd2ec,var(--violet-deep))"></div>
    <div class="brand" style="left:16px;top:14px;font-size:25px"><span class="brand-dot" style="width:42px;height:42px"></span>NorthMerrow</div>
    <p class="tagline" style="bottom:10px;font-size:6.8px">The new materials may be solely used in the North America and distributed in Australia as well. Therefore, we may try something new in these markets.</p>
  </section>

  <!-- Option 5 -->
  <span class="option-number" style="left:35px;top:905px">5</span>
  <section class="card col-left" style="top:983px">
    <div class="map-area" role="img" aria-label="Golden world map with light rays" style="background:linear-gradient(200deg,var(--gold) 0%,var(--sand) 55%,#dde3ea 100%)"></div>
    <div class="brand stacked" style="top:20px;font-size:26px;color:#2e6fb2"><span class="brand-dot" style="width:44px;height:44px"></span>NorthMerrow</div>
    <p class="tagline" style="bottom:8px;color:#2e6fb2;font-size:6.8px">The new materials may be solely used in the North America and distributed in Australia as well. Therefore, we may try something new in these markets.</p>
  </section>

  <!-- Option 6 -->
  <span class="option-number" style="left:376px;top:56px">6</span>
  <section class="card col-right" style="top:58px">
    <div class="map-area" role="img" aria-label="World map across a blue to green gradient" style="background:linear-gradient(180deg,#ffffff 0%,#ffffff 28%,var(--sky-deep) 55%,var(--mint) 100%)"></div>
    <div class="brand" style="left:12px;top:8px;font-size:25px"><span class="brand-dot" style="width:42px;height:42px"></span>NorthMerrow</div>
    <p class="tagline caps" style="bottom:12px;font-size:6.6px">The new materials may be solely used in the North America and distributed in Australia as well. Therefore, we may try something new in these markets.</p>
  </section>

  <!-- Option 7 -->
  <span class="option-number" style="left:376px;top:266px">7</span>
  <section class="card col-right" style="top:291px;background:#eef7fc">
    <div class="band" style="top:0;height:13px;background:#1d7bc8"></div>
    <p class="tagline caps" style="top:3px;text-align:center">Therefore, we may try something new in these markets.</p>
    <div class="map-area" role="img" aria-label="Faint blue world map" style="top:13px;bottom:32px;background:radial-gradient(ellipse at 50% 50%,#ffffff 0 40%,var(--sky) 100%)"></div>
    <div class="brand stacked" style="top:28px;font-size:24px"><span class="brand-dot" style="width:42px;height:42px"></span>NorthMerrow</div>
    <div class="band" style="bottom:0;height:32px;background:linear-gradient(180deg,var(--mint),var(--navy))"></div>
    <p class="tagline caps" style="bottom:9px;text-align:center">The new materials may be solely used in the North America and distributed in Australia as well.</p>
  </section>

  <!-- Option 8 -->
  <span class="option-number" style="left:376px;top:480px">8</span>
  <section class="card col-right" style="top:530px;background:#fbf8fd">
    <div class="map-area" role="img" aria-label="Blue world map" style="top:56px;background:linear-gradient(180deg,#ffffff,var(--sky-deep))"></div>
    <svg class="shape" viewBox="0 0 287 164" preserveAspectRatio="none"><path d="M0 164V92Q0 130 42 130H287V164Z" fill="var(--orange)"/></svg>
    <div class="brand" style="left:12px;top:10px;font-size:25px"><span class="brand-dot" style="width:42px;height:42px"></span>NorthMerrow</div>
    <p class="tagline" style="bottom:8px;padding-left:14px;font-size:6.8px">The new materials may be solely used in the North America and distributed in Australia as well. Therefore, we may try something new in these markets.</p>
  </section>

  <!-- Option 9 -->
  <span class="option-number" style="left:376px;top:718px">9</span>
  <section class="card col-right" style="top:767px;background:var(--olive)">
    <div class="map-area" role="img" aria-label="Sage green world map over skyline" style="bottom:36px;background:linear-gradient(180deg,#e6ebde,var(--sage))"></div>
    <div class="band" style="bottom:34px;height:2px;background:var(--navy)"></div>
    <div class="brand" style="left:12px;top:14px;font-size:25px"><span class="brand-dot" style="width:42px;height:42px"></span>NorthMerrow</div>
    <p class="tagline caps" style="bottom:9px;color:var(--navy);font-size:6.4px">The new materials may be solely used in the North America and distributed in Australia as well. Therefore, we may try something new in these markets.</p>
  </section>

  <!-- Option 10 -->
  <span class="option-number" style="left:358px;top:905px">10</span>
  <section class="card col-right" style="top:983px">
    <div class="map-area" role="img" aria-label="Purple world map over skyline" style="background:linear-gradient(180deg,#e9dcee,var(--violet) 70%,#9a5aa8)"></div>
    <div class="brand" style="right:14px;top:14px;font-size:14px;gap:4px"><span class="brand-dot" style="width:22px;height:22px"></span>NorthMerrow</div>
    <p class="tagline caps" style="bottom:9px;font-size:6.3px">The new materials may be solely used in the North America and distributed in Australia as well. Therefore, we may try something new in these markets.</p>
  </section>

</main>
</body>
</html>
```